Brindle Logistics Business Card Design

We are a trucking and warehousing company. We run freight in the US manly from the Pacific NW to TX and back up the the PNW. We also do warehousing where we store, move, and distribute freight. Looking for a clean and modern design of business card. We would like to look rich and elegant. Attached is our logo.

Industry/Entity Type

Trucking Company

Contact Information for Business Card

Looking for a clean and modern design of business card. We would like to look rich and elegant.

Font styles to use
Sans Serif

Colors

Designer to choose colors to be used in the design.

Requirements
Must have
• logo but it should not dominate the card
Should not have
• logo should not dominate the card

```html
<!DOCTYPE html>
<html lang="en">
<head>
<meta charset="utf-8">
<title>Brindle Logistics Business Card</title>
<link href="https://fonts.googleapis.com/css2?family=Michroma&family=Roboto:wght@400&display=swap" rel="stylesheet">
<style>
  :root {
    --backdrop: #e4e4e4;
    --paper: #f4f4f4;
    --brand-blue: #0f6db5;
    --brand-orange: #f0901c;
    --ink: #4a4a4a;
    --ink-dark: #3c3c3c;
  }
  html, body {
    margin: 0;
    padding: 0;
    width: 1200px;
    height: 960px;
    overflow: hidden;
    background: var(--backdrop);
  }
  .canvas {
    position: relative;
    width: 1200px;
    height: 960px;
  }
  .card {
    position: absolute;
    width: 600px;
    height: 343px;
    background: var(--paper);
    box-shadow: 0 1px 3px rgba(0,0,0,0.25);
  }
  .card-front { left: 314px; top: 113px; }
  .card-back { left: 311px; top: 472px; }

  .person-name {
    position: absolute;
    left: 49px;
    top: 50px;
    margin: 0;
    font-family: "Michroma", sans-serif;
    font-size: 19px;
    font-weight: 400;
    color: var(--brand-blue);
    letter-spacing: 0.5px;
  }
  .person-role {
    position: absolute;
    left: 49px;
    top: 74px;
    margin: 0;
    font-family: "Michroma", sans-serif;
    font-size: 13px;
    color: var(--brand-orange);
    letter-spacing: 0.5px;
  }
  .address {
    position: absolute;
    left: 49px;
    top: 158px;
    margin: 0;
    font-family: "Roboto", sans-serif;
    font-size: 14px;
    line-height: 19px;
    color: var(--ink);
    font-style: normal;
  }
  .contact-list {
    position: absolute;
    left: 49px;
    top: 208px;
    margin: 0;
    padding: 0;
    list-style: none;
    font-family: "Roboto", sans-serif;
    font-size: 14px;
    color: var(--ink);
  }
  .contact-list li {
    display: flex;
    align-items: center;
    height: 19px;
  }
  .contact-list svg {
    width: 14px;
    height: 14px;
    margin-right: 9px;
    fill: var(--brand-blue);
  }
  .front-brand {
    position: absolute;
    right: 42px;
    top: 245px;
    display: flex;
    align-items: center;
    gap: 8px;
    font-family: "Michroma", sans-serif;
    font-size: 11px;
    color: var(--brand-blue);
  }
  .brand-dot {
    width: 26px;
    height: 26px;
    border-radius: 50%;
    background: var(--brand-blue);
  }
  .back-brand {
    position: absolute;
    left: 0;
    right: 0;
    top: 142px;
    display: flex;
    justify-content: center;
    align-items: center;
    gap: 16px;
  }
  .back-brand .brand-dot {
    width: 58px;
    height: 58px;
  }
  .back-brand-name {
    font-family: "Michroma", sans-serif;
    font-size: 30px;
    color: var(--ink-dark);
    letter-spacing: 1px;
  }
</style>
</head>
<body>
<main class="canvas">
  <section class="card card-front">
    <h1 class="person-name">OWEN MARSH</h1>
    <p class="person-role">CEO/FOUNDER</p>
    <address class="address">4120 Cedar Ridge Road<br>Tacoma, Washington 98402</address>
    <ul class="contact-list">
      <li><svg viewBox="0 0 16 16"><path d="M3.6 1.5l2.3 2.6-1.3 1.8c.9 2 2.5 3.6 4.5 4.5l1.8-1.3 2.6 2.3-1.4 2.3C6.8 13.5 2.5 9.2 1.3 3z"/></svg>555 210 4471</li>
      <li><svg viewBox="0 0 16 16"><path d="M4.5 0.5h7v15h-7zM5.8 2v10.5h4.4V2zM8 13.2a.8.8 0 1 0 0 1.6.8.8 0 0 0 0-1.6z"/></svg>555 318 7702</li>
      <li><svg viewBox="0 0 16 16"><path d="M4 1h8v4H4zM1 6h14v7h-3v2H4v-2H1zM5 10v4h6v-4z"/></svg>555 462 0935</li>
      <li><svg viewBox="0 0 16 16"><path d="M1 3.5h14v9H1zM2.3 4.7L8 9l5.7-4.3z" fill-rule="evenodd"/></svg>info@brindlelogistics.com</li>
      <li><svg viewBox="0 0 16 16"><path d="M8 1a7 7 0 1 0 0 14A7 7 0 0 0 8 1zm-1 2.5c1 .8 1.2 2 .4 2.6-.8.6-2.2.1-2.4 1.4-.2 1.1 1.4 1.4 1.6 2.6.2 1-.3 2-.6 2.6A5.4 5.4 0 0 1 7 3.5zm3.5 1c1.8 1.3 2.6 3.6 1.8 5.6-.7-.6-.6-1.7-1.6-2-1.2-.3-1.8-1.2-1.2-2.2.3-.6.8-.9 1-1.4z"/></svg>www.brindlelogistics.com</li>
    </ul>
    <div class="front-brand"><span class="brand-dot"></span><span>Brindle Logistics</span></div>
  </section>

  <section class="card card-back">
    <div class="back-brand">
      <span class="brand-dot"></span>
      <span class="back-brand-name">Brindle Logistics</span>
    </div>
  </section>
</main>
</body>
</html>
```